Studio Business Cards etc
business cards plus
Creative Brief
Use same font as used in my logo
The font Iuse in my log is called "Presidential.ttf"
Modern
Dana Holcrofter
Owner / Cheif Instructor
20381 Brenwick Lane NW #214 Silverdale WA 98383
qplrt@exmailbox.net
http://www.kestonhallstudio.com
I am looking for a new style of layout for my business cards etc. I would be interested in seeing a layout for the standard 3.5x2 as well as a folded card 3.5x 4 The inside could be used for class schedule etc. The name / title would of course be changed depending on our instructors
Concepts
Business card and stationary design. We provide umpires & referees for teams/organizations.

```html
<!DOCTYPE html>
<html lang="en">
<head>
<meta charset="utf-8">
<title>Keston Hall Studio Stationery</title>
<link href="https://fonts.googleapis.com/css2?family=Open+Sans:wght@400;600&display=swap" rel="stylesheet">
<style>
:root{
  --red:#d3202f;
  --red-dark:#b3121f;
  --grey:#8a8a8c;
  --grey-light:#c9c9cb;
  --paper:#ffffff;
  --bg:#f4f4f4;
  --ink:#555559;
  --edge:#e2e2e2;
}
*{margin:0;padding:0;box-sizing:border-box}
html,body{width:1200px;height:936px;overflow:hidden;background:var(--bg);font-family:"Open Sans",Arial,sans-serif;color:var(--ink)}
.piece{position:absolute;background:var(--paper);border:1px solid var(--edge);overflow:hidden}
.piece svg.waves{position:absolute;left:0;top:0;width:100%;height:100%}
.brand{position:absolute;display:flex;align-items:center;gap:6px;color:var(--red);font-weight:600;line-height:1.15}
.brand .dot{flex:none;border:2px solid var(--red);border-radius:50%}
.brand.faint{color:#f1c7cb}
.brand.faint .dot{border-color:#f1c7cb}
.brand.white{color:#fff}
.brand.white .dot{border-color:#fff}
.contact{position:absolute;font-size:6.5px;line-height:1.55;color:var(--ink)}
.contact .icon{display:inline-block;width:5px;height:5px;background:var(--red);border-radius:50%;margin-right:4px;vertical-align:middle}

.letterhead{left:122px;top:33px;width:449px;height:583px}
.folder{left:634px;top:33px;width:465px;height:583px}
.card-front{left:13px;top:731px;width:236px;height:81px;border-radius:6px}
.card-back{left:13px;top:830px;width:236px;height:83px;border-radius:6px;background:var(--red);border-color:var(--red)}
.envelope-front{left:266px;top:680px;width:343px;height:238px}
.envelope-back{left:634px;top:680px;width:463px;height:238px;background:var(--red);border-color:var(--red)}
.web{position:absolute;color:#fff;font-size:12px;letter-spacing:.3px}
</style>
</head>
<body>

<section class="piece letterhead">
  <svg class="waves" viewBox="0 0 449 583" preserveAspectRatio="none">
    <path d="M0 478 Q220 438 449 470 L449 488 Q220 455 0 500 Z" fill="var(--grey)"/>
    <path d="M0 503 Q220 462 449 490 L449 583 L0 583 Z" fill="var(--red)"/>
  </svg>
  <div class="brand" style="left:38px;top:30px;font-size:9px;width:140px">
    <span class="dot" style="width:16px;height:16px"></span>Keston Hall Martial Arts<br>and Fitness Studio
  </div>
  <div class="contact" style="left:262px;top:28px">
    <div><span class="icon"></span>20381 Brenwick Lane NW #214 Silverdale WA 98383</div>
    <div><span class="icon"></span>(360) 555-0148</div>
    <div><span class="icon"></span>(360) 555-0172</div>
    <div><span class="icon"></span>qplrt@exmailbox.net</div>
    <div><span class="icon"></span>http://www.kestonhallstudio.com</div>
  </div>
  <div class="brand faint" style="left:118px;top:270px;font-size:20px;width:260px">
    <span class="dot" style="width:40px;height:40px"></span>Keston Hall Martial Arts<br>and Fitness Studio
  </div>
</section>

<section class="piece folder">
  <svg class="waves" viewBox="0 0 465 583" preserveAspectRatio="none">
    <path d="M0 430 Q230 382 465 410 L465 440 Q230 410 0 462 Z" fill="var(--grey)"/>
    <path d="M0 466 Q230 414 465 444 L465 583 L0 583 Z" fill="var(--red)"/>
  </svg>
  <div class="brand" style="left:100px;top:235px;font-size:21px;width:290px">
    <span class="dot" style="width:48px;height:48px"></span>Keston Hall Martial Arts<br>and Fitness Studio
  </div>
</section>

<section class="piece card-front">
  <svg class="waves" viewBox="0 0 236 81" preserveAspectRatio="none">
    <path d="M0 62 Q118 50 236 58 L236 61 Q118 54 0 66 Z" fill="var(--grey)"/>
    <path d="M0 68 Q118 56 236 63 L236 81 L0 81 Z" fill="var(--red)"/>
  </svg>
  <div class="brand" style="left:10px;top:8px;font-size:6.5px;width:90px">
    <span class="dot" style="width:12px;height:12px"></span>Keston Hall<br>Fitness Studio
  </div>
  <div class="contact" style="left:10px;top:30px;font-size:5px">
    <div>(360) 555-0148</div>
    <div>qplrt@exmailbox.net</div>
  </div>
  <div class="contact" style="left:150px;top:14px;font-size:5.5px;text-align:right;width:78px">
    <div style="font-weight:600;color:var(--red)">Dana Holcrofter</div>
    <div>Owner / Chief Instructor</div>
  </div>
</section>

<section class="piece card-back">
  <div class="brand faint" style="left:70px;top:22px;font-size:10px;width:110px;color:#e46a74">
    <span class="dot" style="width:22px;height:22px;border-color:#e46a74"></span>Keston Hall<br>Fitness Studio
  </div>
  <div class="contact" style="left:10px;top:70px;font-size:5px;color:#fff">www.kestonhallstudio.com</div>
</section>

<section class="piece envelope-front">
  <div class="brand" style="left:18px;top:14px;font-size:9px;width:130px">
    <span class="dot" style="width:18px;height:18px"></span>Keston Hall Martial Arts<br>and Fitness Studio
  </div>
  <div class="contact" style="left:136px;top:22px;font-size:5px">
    <div>20381 Brenwick Lane NW #214</div>
    <div>Silverdale WA 98383</div>
  </div>
</section>

<section class="piece envelope-back">
  <svg class="waves" viewBox="0 0 463 238" preserveAspectRatio="none">
    <path d="M0 0 L463 0 L463 14 Q232 -4 0 14 Z" fill="var(--paper)"/>
    <path d="M0 14 L232 120 L463 14" fill="none" stroke="var(--red-dark)" stroke-width="1"/>
  </svg>
  <div class="web" style="left:170px;top:46px">www.kestonhallstudio.com</div>
</section>

</body>
</html>
```